Company providing Business Management Services needs modern business card

The business provides services like tender preparation, bank submissions, business health checks, financial and admin support. We want to portray 'Trust', 'Strength' and 'Support'.
2 styles of logo in various formats have been uploaded.
Looking for easy to understand, yet sophisticated and stand out from the crowd.

Target Market(s)

Small and Medium sized businesses

Industry/Entity Type

Business

Contact Information for Business Card

Name - Daniel Vesterby, Description - Manager, Phone - 0472 915 603, Email - danielvesterby@kpwholdingsgroup.example, Work description - Business Management Services.

Requirements
Must have
• Logo

```html
<!DOCTYPE html>
<html lang="en">
<head>
<meta charset="utf-8">
<title>KPW Holdings Group – Business Card</title>
<link rel="stylesheet" href="https://fonts.googleapis.com/css2?family=Open+Sans:wght@400;600;700&display=swap">
<style>
  :root {
    --bg: #e9e7e3;
    --card: #ffffff;
    --ink: #3a3a3a;
    --grey: #6b6b6b;
    --logo-grey: #5a5a5a;
    --blue: #2f4594;
  }
  * { box-sizing: border-box; margin: 0; padding: 0; }
  html, body { width: 1200px; height: 913px; overflow: hidden; }
  body {
    background: var(--bg);
    font-family: "Open Sans", Arial, sans-serif;
    color: var(--ink);
    position: relative;
  }
  .card {
    position: absolute;
    left: 280px;
    width: 640px;
    height: 390px;
    background: var(--card);
    box-shadow: 0 6px 18px rgba(0,0,0,0.12);
    overflow: hidden;
  }
  .card--front { top: 40px; }
  .card--back { top: 483px; }

  .brand {
    position: absolute;
    display: flex;
    align-items: center;
    gap: 12px;
  }
  .brand__mark {
    width: 34px; height: 34px;
    background: var(--logo-grey);
    flex: none;
  }
  .brand__name {
    font-weight: 600;
    font-size: 20px;
    color: var(--logo-grey);
    white-space: nowrap;
  }
  .card--front .brand { left: 28px; top: 150px; }
  .card--back .brand {
    left: 50%; top: 50%;
    transform: translate(-50%, -50%);
  }
  .card--back .brand__mark { width: 48px; height: 48px; }
  .card--back .brand__name { font-size: 30px; }

  .values {
    position: absolute;
    right: 40px; top: 28px;
    list-style: none;
    font-size: 13px;
    font-weight: 700;
    letter-spacing: 0.5px;
    line-height: 1.45;
  }
  .values li::before {
    content: "»";
    color: var(--blue);
    margin-right: 6px;
  }
  .values li:nth-child(2) { padding-left: 14px; }
  .values li:nth-child(3) { padding-left: 28px; }

  .contact {
    position: absolute;
    left: 300px; top: 150px;
  }
  .contact__name {
    font-size: 21px;
    font-weight: 700;
    color: var(--blue);
  }
  .contact__role {
    font-size: 14px;
    color: var(--grey);
    margin-bottom: 18px;
  }
  .contact__list { list-style: none; font-size: 13px; line-height: 1.9; }
  .contact__list li { display: flex; align-items: center; gap: 10px; white-space: nowrap; }
  .contact__icon { width: 14px; height: 14px; fill: var(--ink); flex: none; }
  .contact__service { padding-left: 24px; }

  .footer-band {
    position: absolute;
    left: 0; right: 0; bottom: 0;
    height: 16px;
    background: var(--blue);
  }
</style>
</head>
<body>

<section class="card card--front">
  <div class="brand">
    <span class="brand__mark"></span>
    <span class="brand__name">KPW Holdings Group</span>
  </div>

  <ul class="values">
    <li>TRUST</li>
    <li>STRENGTH</li>
    <li>SUPPORT</li>
  </ul>

  <div class="contact">
    <p class="contact__name">Daniel Vesterby</p>
    <p class="contact__role">Manager</p>
    <ul class="contact__list">
      <li>
        <svg class="contact__icon" viewBox="0 0 16 16" aria-hidden="true"><path d="M1 5c0-2 3-3 7-3s7 1 7 3v1h-3V5H4v1H1z M3 7h10l1 7H2z"/></svg>
        0472 915 603
      </li>
      <li>
        <svg class="contact__icon" viewBox="0 0 16 16" aria-hidden="true"><circle cx="8" cy="8" r="7"/><path d="M1 8h14M8 1c3 3 3 11 0 14M8 1c-3 3-3 11 0 14" stroke="#fff" stroke-width="1" fill="none"/></svg>
        www.kpwholdingsgroup.example
      </li>
      <li>
        <svg class="contact__icon" viewBox="0 0 16 16" aria-hidden="true"><rect x="1" y="3" width="14" height="10"/><path d="M1 3l7 6 7-6" stroke="#fff" stroke-width="1.2" fill="none"/></svg>
        danielvesterby@kpwholdingsgroup.example
      </li>
      <li class="contact__service">Business Management Services</li>
    </ul>
  </div>

  <div class="footer-band"></div>
</section>

<section class="card card--back">
  <div class="brand">
    <span class="brand__mark"></span>
    <span class="brand__name">KPW Holdings Group</span>
  </div>
</section>

</body>
</html>
```